Brindley Health Care Association Needs Your Help!

Hello, we are a non-profit association dedicated to supporting our members' ability to create a better healthcare system. All of our members are Brindley alumni working in healthcare. As part of this, we're looking to update the banner on our email newsletter to look fresher and more official. Please help us out!

Target Market(s)

Higher Education, Healthcare

Industry/Entity Type

Healthcare

Font styles to use
Serif

Colors
0255a3
ec1f27
ffffff

Requirements
Must have
• Please incorporate the standard Brindley Logo
Nice to have
• If you took the attached "logo 2" which has the Brindley logo and the "Medical Leadership Graduates Society" in red serif font as your starting point, we'd be pretty happy with something that builds on that.
Should not have
• Don't get too creative or abstract.

```html
<!DOCTYPE html>
<html lang="en">
<head>
<meta charset="utf-8">
<title>Brindley Alumni – Newsletter Banners</title>
<link rel="stylesheet" href="https://fonts.googleapis.com/css2?family=Libre+Baskerville&display=swap">
<style>
  :root {
    --crimson: #a8082f;
    --crimson-deep: #8a0628;
    --navy: #1f3f7a;
    --navy-deep: #123066;
    --plum: #4a2358;
    --white: #ffffff;
    --page: #ffffff;
  }
  * { margin: 0; padding: 0; box-sizing: border-box; }
  html, body {
    width: 702px;
    height: 1200px;
    overflow: hidden;
    background: var(--page);
  }
  .banner-set {
    position: relative;
    width: 702px;
    height: 1200px;
  }
  .banner {
    position: absolute;
    left: 118px;
    width: 472px;
    height: 184px;
    display: block;
  }
  .banner--team     { top: 45px; }
  .banner--meeting  { top: 274px; }
  .banner--surgeon  { top: 494px; }
  .banner--table    { top: 713px; }
  .banner--xray     { top: 933px; }
  .banner-title, .brand-name {
    font-family: "Libre Baskerville", Georgia, serif;
    fill: var(--white);
  }
  .banner-title { font-size: 16px; letter-spacing: 2px; }
  .brand-name { font-size: 17px; }
  .brand-name--small { font-size: 15px; }
</style>
</head>
<body>
<main class="banner-set">

  <!-- Banner: team portrait -->
  <svg class="banner banner--team" viewBox="0 0 592 231" aria-labelledby="t1">
    <title id="t1">Medical Leadership Graduates Society banner with care team</title>
    <defs>
      <linearGradient id="photoTeam" x1="0" y1="0" x2="1" y2="1">
        <stop offset="0" stop-color="#d9dde2"/>
        <stop offset="0.5" stop-color="#eef0f2"/>
        <stop offset="1" stop-color="#6f94c6"/>
      </linearGradient>
      <linearGradient id="crimsonSweep" x1="0" y1="0" x2="1" y2="0">
        <stop offset="0" stop-color="var(--crimson)"/>
        <stop offset="0.6" stop-color="#7e0a36"/>
        <stop offset="1" stop-color="var(--plum)"/>
      </linearGradient>
    </defs>
    <rect class="banner-photo" width="592" height="231" fill="url(#photoTeam)" role="img" aria-label="Photo of a smiling healthcare team in white coats and blue scrubs"/>
    <path class="banner-band" d="M0,0 L20,0 C180,70 330,170 592,185 L592,231 L0,231 Z" fill="var(--navy)"/>
    <path class="banner-field" d="M0,12 C160,90 330,188 592,205 L592,231 L0,231 Z" fill="url(#crimsonSweep)"/>
    <g class="brand">
      <rect x="15" y="100" width="20" height="20" fill="var(--white)"/>
      <text class="brand-name" x="42" y="117">Brindley Alumni</text>
    </g>
    <text class="banner-title">
      <tspan x="15" y="159">MEDICAL LEADERSHIP</tspan>
      <tspan x="15" y="181">GRADUATES</tspan>
      <tspan x="15" y="203">SOCIETY</tspan>
    </text>
  </svg>

  <!-- Banner: team discussion -->
  <svg class="banner banner--meeting" viewBox="0 0 592 231" aria-labelledby="t2">
    <title id="t2">Medical Leadership Graduates Society banner with team discussion</title>
    <defs>
      <linearGradient id="photoMeeting" x1="0" y1="0" x2="1" y2="0">
        <stop offset="0" stop-color="#8c9199"/>
        <stop offset="0.5" stop-color="#b9c3cc"/>
        <stop offset="1" stop-color="#d8dce0"/>
      </linearGradient>
      <linearGradient id="crimsonFade" x1="0" y1="0" x2="1" y2="0">
        <stop offset="0" stop-color="var(--crimson)"/>
        <stop offset="1" stop-color="var(--plum)"/>
      </linearGradient>
    </defs>
    <rect class="banner-photo" width="592" height="231" fill="url(#photoMeeting)" role="img" aria-label="Photo of doctors and nurses in discussion around a table"/>
    <path class="banner-band" d="M0,28 C150,110 330,160 592,165 L592,231 L0,231 Z" fill="var(--navy-deep)"/>
    <path class="banner-field" d="M0,105 C120,150 260,205 420,231 L0,231 Z" fill="url(#crimsonFade)"/>
    <text class="banner-title">
      <tspan x="15" y="159">MEDICAL LEADERSHIP</tspan>
      <tspan x="15" y="181">GRADUATES</tspan>
      <tspan x="15" y="203">SOCIETY</tspan>
    </text>
    <g class="brand">
      <rect x="428" y="199" width="16" height="16" fill="var(--white)"/>
      <text class="brand-name brand-name--small" x="578" y="213" text-anchor="end">Brindley Alumni</text>
    </g>
  </svg>

  <!-- Panel banners -->
  <svg class="banner banner--surgeon" viewBox="0 0 592 231" aria-labelledby="t3">
    <title id="t3">Medical Leadership Graduates Society banner with surgeon at monitor</title>
    <defs>
      <linearGradient id="photoSurgeon" x1="0" y1="0" x2="1" y2="0">
        <stop offset="0" stop-color="#2c3f5c"/>
        <stop offset="0.6" stop-color="#7f95ad"/>
        <stop offset="1" stop-color="#4a5f78"/>
      </linearGradient>
    </defs>
    <rect width="592" height="231" fill="var(--crimson)"/>
    <path d="M190,0 C160,80 170,170 220,231 L592,231 L592,0 Z" fill="var(--crimson-deep)"/>
    <path d="M300,0 C230,60 215,170 275,231 L592,231 L592,0 Z" fill="var(--navy)"/>
    <path class="banner-photo" d="M292,0 C255,60 250,170 285,231 L592,231 L592,0 Z" fill="url(#photoSurgeon)" role="img" aria-label="Photo of a surgeon in scrubs and mask checking a medical monitor"/>
    <g class="brand">
      <rect x="27" y="35" width="24" height="24" fill="var(--white)"/>
      <text class="brand-name" x="58" y="54">Brindley Alumni</text>
    </g>
    <text class="banner-title">
      <tspan x="26" y="117">MEDICAL</tspan>
      <tspan x="26" y="139">LEADERSHIP</tspan>
      <tspan x="26" y="161">GRADUATES</tspan>
      <tspan x="26" y="183">SOCIETY</tspan>
    </text>
  </svg>

  <svg class="banner banner--table" viewBox="0 0 592 231" aria-labelledby="t4">
    <title id="t4">Medical Leadership Graduates Society banner with clinical meeting</title>
    <defs>
      <linearGradient id="photoTable" x1="0" y1="0" x2="1" y2="1">
        <stop offset="0" stop-color="#9aa4ad"/>
        <stop offset="0.5" stop-color="#cfd6dd"/>
        <stop offset="1" stop-color="#e9ecef"/>
      </linearGradient>
    </defs>
    <rect width="592" height="231" fill="var(--crimson)"/>
    <path d="M190,0 C160,80 170,170 220,231 L592,231 L592,0 Z" fill="var(--crimson-deep)"/>
    <path d="M300,0 C230,60 215,170 275,231 L592,231 L592,0 Z" fill="var(--navy)"/>
    <path class="banner-photo" d="M292,0 C255,60 250,170 285,231 L592,231 L592,0 Z" fill="url(#photoTable)" role="img" aria-label="Photo of a medical team meeting at a table with a laptop"/>
    <g class="brand">
      <rect x="27" y="35" width="24" height="24" fill="var(--white)"/>
      <text class="brand-name" x="58" y="54">Brindley Alumni</text>
    </g>
    <text class="banner-title">
      <tspan x="26" y="117">MEDICAL</tspan>
      <tspan x="26" y="139">LEADERSHIP</tspan>
      <tspan x="26" y="161">GRADUATES</tspan>
      <tspan x="26" y="183">SOCIETY</tspan>
    </text>
  </svg>

  <svg class="banner banner--xray" viewBox="0 0 592 231" aria-labelledby="t5">
    <title id="t5">Medical Leadership Graduates Society banner with chest x-ray tablet</title>
    <defs>
      <linearGradient id="photoXray" x1="0" y1="0" x2="1" y2="1">
        <stop offset="0" stop-color="#c7ccd2"/>
        <stop offset="0.5" stop-color="#8fa6bd"/>
        <stop offset="1" stop-color="#dfe3e7"/>
      </linearGradient>
    </defs>
    <rect width="592" height="231" fill="var(--crimson)"/>
    <path d="M190,0 C160,80 170,170 220,231 L592,231 L592,0 Z" fill="var(--crimson-deep)"/>
    <path d="M300,0 C230,60 215,170 275,231 L592,231 L592,0 Z" fill="var(--navy)"/>
    <path class="banner-photo" d="M292,0 C255,60 250,170 285,231 L592,231 L592,0 Z" fill="url(#photoXray)" role="img" aria-label="Photo of a tablet showing a chest x-ray on a desk with stethoscope and gloves"/>
    <g class="brand">
      <rect x="27" y="35" width="24" height="24" fill="var(--white)"/>
      <text class="brand-name" x="58" y="54">Brindley Alumni</text>
    </g>
    <text class="banner-title">
      <tspan x="26" y="117">MEDICAL</tspan>
      <tspan x="26" y="139">LEADERSHIP</tspan>
      <tspan x="26" y="161">GRADUATES</tspan>
      <tspan x="26" y="183">SOCIETY</tspan>
    </text>
  </svg>

</main>
</body>
</html>
```